Tarn - Stationary Design/Layout

We are a well established clothing design and manufacturing company (Tarn Sourcing) based in London UK, with our own factory in Bangladesh, supplying to many fashion retailers and brands. Our factory has very high environmental and ethical standards with people at its heart. Our quality of garments are second to none.
Our new logo has been proudly developed by the Pixel Guild community last month, we are now in the second phase and need the layout designed for our letterheads, double sided business cards, compliment slip and clothing ticket. Feel as creative as you like, but make sure it looks great!!
***The Logo - the logo design and colour is set and should NOT be changed and stay on a dark grey backround. The logo artwork to use is attached.
***Details to use for the business card:
Dorian Pelham
Direct Line: 020 7946 0158
dorian@tarnsourcing-example.com
Tarn Sourching Ltd.
57 - 59 Hollin Row
Ashcombe . Kelbridge
NW9 4QT
Switchboard: 020 7946 0274
Fax: 020 7946 0274
www.tarnsourcing-example.co.uk
***Details to use for the letterhead and compliment slip:
Tarn Sourching Ltd.
57 - 59 Hollin Row
Ashcombe . Kelbridge
NW9 4QT
Fax: 020 7946 0274
www.tarnsourcing-example.co.uk
***Details for Swing Ticket:
Size: 12cm height by 5.5cm width
One side need to have just the logo without the 'Sourcing', on the other it needs to stay blank

```html
<!DOCTYPE html>
<html lang="en">
<head>
<meta charset="utf-8">
<title>Tarn Sourcing – Stationery Set</title>
<link rel="stylesheet" href="https://fonts.googleapis.com/css2?family=Questrial&display=swap">
<style>
  :root {
    --brand-blue: #96cfdc;
    --brand-grey: #3a3a3a;
    --paper: #ffffff;
    --ink: #3a3a3a;
  }
  * { box-sizing: border-box; margin: 0; padding: 0; }
  html, body {
    width: 1200px; height: 933px; overflow: hidden;
    background: var(--paper);
    font-family: "Questrial", "Century Gothic", sans-serif;
    color: var(--ink);
  }
  .sheet { position: relative; width: 1200px; height: 933px; }
  .piece { position: absolute; background: var(--brand-blue); }
  .paper { position: absolute; background: var(--paper); }
  .brand-block {
    position: absolute; background: var(--brand-grey);
    display: flex; align-items: center; justify-content: center;
  }
  .brand-name {
    color: var(--brand-blue); font-weight: 400;
    text-transform: uppercase; white-space: nowrap;
  }

  /* Business card front */
  .card-front { left: 81px; top: 78px; width: 220px; height: 144px; }
  .card-front .paper { left: 11px; top: 12px; width: 198px; height: 121px; }
  .card-front .brand-block { left: 63px; top: 0; width: 94px; height: 40px; }
  .card-front .brand-name { font-size: 10px; letter-spacing: 1px; }
  .card-person { position: absolute; left: 17px; top: 67px; font-size: 5px; line-height: 7.5px; white-space: nowrap; }
  .card-person .name { font-size: 10px; color: var(--brand-blue); line-height: 13px; }
  .card-company { position: absolute; left: 122px; top: 68px; font-size: 5px; line-height: 6.8px; white-space: nowrap; }
  .card-company strong, .card-company .web { font-weight: 700; }
  .card-company .gap { height: 8px; }

  /* Business card back */
  .card-back { left: 332px; top: 78px; width: 220px; height: 144px; }
  .card-back .brand-block { left: 17px; top: 24px; width: 183px; height: 76px; }
  .card-back .brand-name { font-size: 19px; letter-spacing: 2px; }
  .card-back .web {
    position: absolute; left: 0; right: 0; top: 115px; text-align: center;
    font-size: 7.5px; letter-spacing: 1.6px;
  }

  /* Compliment slip */
  .comp-slip { left: 81px; top: 253px; width: 471px; height: 262px; }
  .comp-slip .paper { left: 20px; top: 20px; width: 432px; height: 222px; }
  .comp-slip .brand-block { left: 170px; top: 0; width: 131px; height: 55px; }
  .comp-slip .brand-name { font-size: 13px; letter-spacing: 1.5px; }
  .slip-footer {
    position: absolute; left: 0; right: 0; top: 214px; text-align: center;
    font-size: 5.6px; line-height: 10px; white-space: nowrap;
  }

  /* Swing tickets */
  .ticket {
    position: absolute; top: 542px; width: 144px; height: 314px;
    clip-path: polygon(28px 0, 116px 0, 144px 31px, 144px 100%, 0 100%, 0 31px);
  }
  .ticket-front { left: 171px; background: var(--brand-blue); }
  .ticket-back { left: 330px; background: var(--brand-grey); }
  .ticket-hole {
    position: absolute; left: 61px; top: 14px; width: 22px; height: 22px;
    border-radius: 50%; background: var(--paper);
  }
  .ticket-front .brand-block { left: 25px; top: 65px; width: 95px; height: 223px; }
  .ticket-front .brand-name { font-size: 54px; letter-spacing: 6px; transform: rotate(90deg); }

  /* Letterhead */
  .letterhead { left: 577px; top: 79px; width: 549px; height: 776px; }
  .letterhead .paper { left: 24px; top: 25px; width: 502px; height: 726px; }
  .letterhead .brand-block { left: 196px; top: 0; width: 157px; height: 66px; }
  .letterhead .brand-name { font-size: 15px; letter-spacing: 1.8px; }
  .letter-footer {
    position: absolute; left: 0; right: 0; top: 711px; text-align: center;
    font-size: 10.3px; line-height: 17px; white-space: nowrap;
  }
  .sep { padding: 0 8px; }
  .slip-footer .sep { padding: 0 5px; }
  .web-strong { font-weight: 700; }
</style>
</head>
<body>
<main class="sheet">

  <section class="piece card-front" aria-label="Business card front">
    <div class="paper"></div>
    <div class="brand-block"><span class="brand-name">Tarn Sourcing</span></div>
    <div class="card-person">
      <div class="name">Dorian Pelham</div>
      Direct Line: 020 7946 0158<br>
      dorian@tarnsourcing-example.com
    </div>
    <div class="card-company">
      <strong>Tarn Sourching Ltd.</strong><br>
      57 - 59 Hollin Row<br>
      Ashcombe . Kelbridge<br>
      NW9 4QT
      <div class="gap"></div>
      Switchboard: 020 7946 0274<br>
      Fax: 020 7946 0274<br>
      <span class="web">www.tarnsourcing-example.co.uk</span>
    </div>
  </section>

  <section class="piece card-back" aria-label="Business card back">
    <div class="brand-block"><span class="brand-name">Tarn Sourcing</span></div>
    <p class="web">www.tarnsourcing-example.co.uk</p>
  </section>

  <section class="piece comp-slip" aria-label="Compliment slip">
    <div class="paper"></div>
    <div class="brand-block"><span class="brand-name">Tarn Sourcing</span></div>
    <div class="slip-footer">
      Tarn Sourching Ltd. 57 - 59 Hollin Row, Ashcombe . Kelbridge, NW9 4QT<br>
      Switchboard: 020 7946 0274<span class="sep">|</span>Fax: 020 7946 0274<span class="sep">|</span><span class="web-strong">www.tarnsourcing-example.co.uk</span>
    </div>
  </section>

  <section class="ticket ticket-front" aria-label="Swing ticket front">
    <div class="ticket-hole"></div>
    <div class="brand-block"><span class="brand-name">Tarn</span></div>
  </section>

  <section class="ticket ticket-back" aria-label="Swing ticket back">
    <div class="ticket-hole"></div>
  </section>

  <section class="piece letterhead" aria-label="Letterhead">
    <div class="paper"></div>
    <div class="brand-block"><span class="brand-name">Tarn Sourcing</span></div>
    <div class="letter-footer">
      Tarn Sourching Ltd. 57 - 59 Hollin Row, Ashcombe . Kelbridge, NW9 4QT<br>
      Switchboard: 020 7946 0274<span class="sep">|</span>Fax: 020 7946 0274<span class="sep">|</span><span class="web-strong">www.tarnsourcing-example.co.uk</span>
    </div>
  </section>

</main>
</body>
</html>
```